Large walking and cycling programme needs a vision poster

We need a visually inspiring poster that promotes the Kestrel Pathways Programmes' vision, key priorities and values. The Kestrel Pathways Programme is a large project in Auckland that will deliver more walking and cycling infrastructure to the city. <br/>Elements that need to be included in the poster are:<br/>Vision - Choice connections for our communities<br/>Key priorities - Our story, Smarter procurement, Our resources<br/>Values - Courageous, Communication, Just do it, Own the bigger programme, Openness and collaboration, Flexibility and open to change

```html
<!DOCTYPE html>
<html lang="en">
<head>
<meta charset="utf-8">
<title>Kestrel Pathways Programmes – Vision Poster</title>
<link rel="stylesheet" href="https://fonts.googleapis.com/css2?family=Barlow+Condensed:wght@500;600;700&display=swap">
<style>
  :root {
    --backdrop: #9a9b9f;
    --ink: #1b1b1c;
    --blue-deep: #1375c0;
    --blue-light: #9fdbeb;
    --white: #ffffff;
    --photo-sky: #d9e4ea;
    --photo-grass: #5f8a4a;
  }
  * { margin: 0; padding: 0; box-sizing: border-box; }
  html, body { width: 998px; height: 1200px; overflow: hidden; background: var(--backdrop); }
  .canvas { position: relative; width: 998px; height: 1200px; }
  .poster {
    position: absolute; left: 82px; top: 12px;
    width: 833px; height: 1175px;
    background: var(--ink); overflow: hidden;
    font-family: "Barlow Condensed", "Arial Narrow", sans-serif;
    color: var(--white);
  }
  .poster__art { position: absolute; left: 0; top: 0; width: 833px; height: 600px; }
  .brand {
    position: absolute; left: 58px; top: 632px;
    font-size: 46px; font-weight: 700; letter-spacing: 0.5px;
    text-transform: uppercase; color: var(--white);
  }
  .intro { position: absolute; left: 55px; top: 760px; width: 300px; }
  .intro__heading {
    border-top: 2px solid var(--blue-light);
    border-bottom: 2px solid var(--blue-light);
    color: var(--blue-light);
    font-size: 38px; font-weight: 600; line-height: 50px;
    text-transform: uppercase; letter-spacing: 0.3px;
  }
  .intro__vision {
    margin-top: 10px; font-size: 21px; font-weight: 700;
    line-height: 25px; text-transform: uppercase; color: var(--white);
  }
  .intro__group { margin-top: 12px; }
  .intro__label {
    font-size: 17px; font-weight: 700; line-height: 21px;
    text-transform: uppercase; letter-spacing: 0.6px; color: var(--blue-light);
  }
  .intro__list {
    font-size: 19px; font-weight: 600; line-height: 23px;
    font-variant: small-caps; color: var(--white);
  }
  .title {
    position: absolute; right: 45px; top: 708px;
    text-align: right; text-transform: uppercase; font-weight: 700;
  }
  .title__line { display: block; line-height: 0.98; }
  .title__line--lead { font-size: 116px; color: var(--blue-deep); }
  .title__line--mid { font-size: 100px; color: var(--blue-deep); }
  .title__line--sub { font-size: 74px; font-weight: 600; color: var(--blue-light); margin-top: 4px; }
  .divider { position: absolute; left: 20px; top: 1091px; width: 788px; height: 3px; background: var(--white); }
  .contacts {
    position: absolute; left: 64px; right: 46px; top: 1118px;
    display: flex; justify-content: space-between; align-items: center;
    font-size: 22px; font-weight: 600; font-variant: small-caps;
    color: var(--blue-light);
  }
  .contact { display: flex; align-items: center; gap: 12px; }
  .contact__mark { width: 26px; height: 26px; flex: none; }
  .contact__mark--square { background: var(--blue-light); border-radius: 3px; }
  .contact__mark--circle { background: var(--blue-light); border-radius: 50%; width: 32px; height: 32px; }
</style>
</head>
<body>
<div class="canvas">
  <article class="poster">
    <svg class="poster__art" viewBox="0 0 833 600">
      <defs>
        <linearGradient id="photoTone" x1="0" y1="0" x2="0" y2="1">
          <stop offset="0" stop-color="var(--photo-sky)"/>
          <stop offset="0.45" stop-color="#8aa07a"/>
          <stop offset="1" stop-color="var(--photo-grass)"/>
        </linearGradient>
      </defs>
      <polygon role="img" aria-label="Photo of three cyclists in helmets with mountain bikes on a grassy trail"
        fill="url(#photoTone)"
        points="0,0 833,0 833,400 375,545 0,185"/>
      <polygon class="band band--deep" fill="var(--blue-deep)" points="108,0 488,0 623,75"/>
      <polygon class="band band--light" fill="var(--blue-light)" points="488,0 808,0 623,75"/>
      <polygon class="band band--light" fill="var(--blue-light)" points="0,185 375,545 355,597 0,365"/>
      <polygon class="band band--deep" fill="var(--blue-deep)" points="0,365 355,597 0,525"/>
      <polygon class="band band--light" fill="var(--blue-light)" points="375,545 833,400 833,562 355,597"/>
      <polygon class="base" fill="var(--ink)" points="0,525 355,597 833,562 833,600 0,600"/>
    </svg>

    <div class="brand">Kestrel Pathways</div>

    <section class="intro">
      <h2 class="intro__heading">Our vision</h2>
      <p class="intro__vision">Choice connections for our communities</p>
      <div class="intro__group">
        <h3 class="intro__label">Key priorities</h3>
        <p class="intro__list">Our story · Smarter procurement · Our resources</p>
      </div>
      <div class="intro__group">
        <h3 class="intro__label">Our values</h3>
        <p class="intro__list">Courageous · Communication · Just do it · Own the bigger programme · Openness and collaboration · Flexibility and open to change</p>
      </div>
    </section>

    <h1 class="title">
      <span class="title__line title__line--lead">Kestrel</span>
      <span class="title__line title__line--mid">Pathways</span>
      <span class="title__line title__line--sub">Programmes</span>
    </h1>

    <div class="divider"></div>

    <footer class="contacts">
      <div class="contact">
        <svg class="contact__mark" viewBox="0 0 24 34" style="height:34px" aria-hidden="true">
          <path d="M12 0C5.4 0 0 5.2 0 11.7 0 20 12 34 12 34s12-14 12-22.3C24 5.2 18.6 0 12 0z" fill="var(--blue-light)"/>
          <circle cx="12" cy="11.5" r="4.5" fill="var(--ink)"/>
        </svg>
        <span>Auckland, New Zealand</span>
      </div>
      <div class="contact">
        <span class="contact__mark contact__mark--square"></span>
        <span>Walk · Cycle · Connect</span>
      </div>
      <div class="contact">
        <span class="contact__mark contact__mark--circle"></span>
        <span>09 555 0142</span>
      </div>
    </footer>
  </article>
</div>
</body>
</html>
```